Under 16 Cricket Tour To Malaysia

I need a flyer to promote an under 16 cricket to Malaysia
The tour will run from April 25th 2108 to May the 7th

Target Market(s)

Boys aged 15-16

Industry/Entity Type

Tour

Font styles to use
Serif

Colors
0255a3
ec1f27

Requirements
Must have
• Dates of the tour
• T20 and Limited Overs games against teams from 5 other countries.
• Name of the tournament is Pelangi Invitational Under 16 Cricket Tournament
• Level 3 coaches with international experience
• Contact Marcus at marcus@brightwickathletics.com.au for more information.

```html
<!DOCTYPE html>
<html lang="en">
<head>
<meta charset="utf-8">
<title>Pelangi Invitational Under 16 Cricket Tournament</title>
<link rel="stylesheet" href="https://fonts.googleapis.com/css2?family=Bebas+Neue&family=Roboto:wght@400&display=swap">
<style>
  :root{
    --blue:#324496;
    --red:#e3062b;
    --white:#ffffff;
    --yellow:#eabc2e;
    --yellow-deep:#d9a824;
    --grey:#a5a5a5;
    --ink:#111111;
    --navy:#1d2a6b;
    --black:#161616;
    --canvas:#ffffff;
  }
  *{margin:0;padding:0;box-sizing:border-box}
  html,body{width:1200px;height:1200px;overflow:hidden;background:var(--canvas)}
  .canvas{position:relative;width:1200px;height:1200px;background:var(--canvas)}
  .flyer{position:absolute;left:179px;top:11px;width:818px;height:1164px;overflow:hidden}

  .hero{position:absolute;left:0;top:0;width:818px;height:983px;overflow:hidden;background:var(--blue)}
  .hero-bands{position:absolute;left:0;top:0;width:818px;height:983px;z-index:0}
  .player-art{position:absolute;left:125px;top:300px;width:290px;height:683px;z-index:1;
    background:linear-gradient(180deg,var(--yellow),var(--yellow-deep));border-radius:145px 145px 16px 16px}

  .skewed{position:absolute;z-index:2;color:var(--white);font-family:"Bebas Neue",sans-serif;font-weight:400;
    transform-origin:0 0;transform:skewY(-22deg);white-space:nowrap}
  .title{left:46px;top:281px;font-size:66px;line-height:1}
  .dates{left:403px;top:388px;font-size:48px;line-height:1}
  .fixtures{left:280px;top:508px;width:469px;font-size:39px;line-height:1.15;text-align:right}
  .coaches{left:390px;top:692px;font-size:43px;line-height:1.25}

  .footer{position:absolute;left:0;top:983px;width:818px;height:181px;background:var(--grey)}
  .contact{position:absolute;left:55px;top:36px;color:var(--ink)}
  .contact-line{font-family:"Bebas Neue",sans-serif;font-size:36px;line-height:1}
  .contact-email{font-family:"Roboto",sans-serif;font-size:22px;line-height:1;margin:12px 0 12px}
  .sponsor{position:absolute;top:48px;height:77px;display:flex;align-items:center;justify-content:center;
    font-family:"Bebas Neue",sans-serif;text-align:center;line-height:1}
  .sponsor-retail{left:435px;width:185px;background:var(--white);color:var(--navy);font-size:24px}
  .sponsor-club{left:643px;width:111px;background:var(--black);color:var(--white);font-size:16px;gap:6px;flex-direction:column}
  .sponsor-dot{width:18px;height:18px;border-radius:50%;background:var(--white)}
</style>
</head>
<body>
<div class="canvas">
  <div class="flyer">
    <section class="hero">
      <svg class="hero-bands" viewBox="0 0 818 983" aria-hidden="true">
        <defs>
          <clipPath id="red-field">
            <polygon points="678,0 818,0 818,983 300,983"/>
          </clipPath>
        </defs>
        <polygon points="678,0 818,0 818,983 300,983" fill="var(--red)"/>
        <g clip-path="url(#red-field)" fill="var(--white)">
          <polygon points="818,63 818,100 0,430 0,393"/>
          <polygon points="818,266 818,296 0,626 0,596"/>
          <polygon points="818,440 818,472 0,802 0,770"/>
          <polygon points="818,660 818,694 0,1024 0,990"/>
          <polygon points="818,780 818,814 0,1144 0,1110"/>
        </g>
      </svg>
      <div class="player-art" role="img" aria-label="Illustration of a young batsman in yellow, mid-swing with bat raised"></div>
      <h1 class="skewed title">Pelangi Invitational Under 16<br>Cricket Tournament</h1>
      <p class="skewed dates">April 25 to May 7 2018</p>
      <p class="skewed fixtures">T20 and limited overs games against<br>teams from 5 other countries</p>
      <p class="skewed coaches">Level 3 coaches with<br>international experience</p>
    </section>
    <footer class="footer">
      <div class="contact">
        <p class="contact-line">Contact Marcus at</p>
        <p class="contact-email">marcus@brightwickathletics.com.au</p>
        <p class="contact-line">For more information</p>
      </div>
      <div class="sponsor sponsor-retail">Harbourline Sport<br>Seaford</div>
      <div class="sponsor sponsor-club"><span class="sponsor-dot"></span>Brightwick Athletics</div>
    </footer>
  </div>
</div>
</body>
</html>
```